Business Card Design

Its a residential construction company

Industry/Entity Type

Residential

Contact Information for Business Card

Belvora Homes Pty Ltd,
Dylan R Foster
BE (Civil), Grad.Dip Hwy, Eng. (QCTU), FTC.Aust,
Director, Belvora Homes Pty Ltd

PO Box 587, Tarrowby, NSW, 2741. Tel: 048765 2231
email: dylan@belvorahomes.com

```html
<!DOCTYPE html>
<html lang="en">
<head>
<meta charset="utf-8">
<title>Belvora Homes – Business Card</title>
<link rel="stylesheet" href="https://fonts.googleapis.com/css2?family=Libre+Franklin:wght@400;700&display=swap">
<style>
  :root {
    --backdrop: #ececec;
    --navy: #062f66;
    --orange: #f08a12;
    --white: #ffffff;
    --wood-light: #e9a257;
    --wood-mid: #c97a2c;
    --wood-dark: #8a4d17;
  }
  * { margin: 0; padding: 0; box-sizing: border-box; }
  html, body {
    width: 1200px; height: 963px; overflow: hidden;
    background: var(--backdrop);
    font-family: "Libre Franklin", Arial, sans-serif;
  }
  .card {
    position: absolute; left: 150px; top: 206px;
    width: 900px; height: 550px;
    background: var(--navy);
    overflow: hidden;
    box-shadow: 0 6px 24px rgba(0,0,0,.18);
  }
  .card__photo {
    position: absolute; left: 0; top: 0; width: 430px; height: 100%;
    background:
      linear-gradient(90deg, rgba(120,70,10,.35) 0%, rgba(0,0,0,0) 40%),
      linear-gradient(160deg, var(--wood-light) 0%, var(--wood-mid) 55%, var(--wood-dark) 100%);
  }
  .card__panel {
    position: absolute; left: 430px; top: 0; right: 0; bottom: 0;
    color: var(--white);
  }
  .name-band {
    position: absolute; left: 0; right: 0; top: 55px; height: 82px;
    background: var(--orange);
    color: var(--navy);
    padding: 14px 0 0 22px;
  }
  .name-band__name { font-weight: 700; font-size: 29px; line-height: 1.1; }
  .name-band__role { font-size: 21px; line-height: 1.3; }
  .credentials {
    position: absolute; left: 22px; top: 150px;
    font-size: 21px; line-height: 1.4;
  }
  .company {
    position: absolute; left: 22px; top: 268px;
    font-weight: 700; font-size: 25px;
  }
  .contact-list {
    position: absolute; left: 22px; top: 310px;
    list-style: none; font-size: 21px;
  }
  .contact-list li { display: flex; align-items: center; height: 36px; white-space: nowrap; }
  .contact-list svg { width: 22px; height: 22px; margin-right: 12px; flex: none; }
</style>
</head>
<body>
  <section class="card" aria-label="Business card">
    <div class="card__photo" role="img" aria-label="Photo of a brass door lock with a key and a red house-shaped key ring"></div>
    <div class="card__panel">
      <div class="name-band">
        <div class="name-band__name">Dylan R Foster</div>
        <div class="name-band__role">Director</div>
      </div>
      <p class="credentials">BE (Civil), Grad.Dip Hwy,<br>Eng. (QCTU), FTC.Aust,</p>
      <p class="company">Belvora Homes Pty Ltd</p>
      <ul class="contact-list">
        <li>
          <svg viewBox="0 0 24 24" aria-hidden="true"><circle cx="12" cy="12" r="11" fill="#fff"/><path d="M12 5a4.5 4.5 0 0 0-4.5 4.5C7.5 13 12 18.5 12 18.5s4.5-5.5 4.5-9A4.5 4.5 0 0 0 12 5zm0 6.2a1.7 1.7 0 1 1 0-3.4 1.7 1.7 0 0 1 0 3.4z" fill="#062f66"/></svg>
          PO Box 587, Tarrowby, NSW, 2741.
        </li>
        <li>
          <svg viewBox="0 0 24 24" aria-hidden="true"><circle cx="12" cy="12" r="11" fill="#fff"/><path d="M9 6.5l1.6 3-1.2 1.2a8 8 0 0 0 3.9 3.9l1.2-1.2 3 1.6-.8 2.3c-5 .3-9.9-4.6-9.6-9.6z" fill="#062f66"/></svg>
          048765 2231
        </li>
        <li>
          <svg viewBox="0 0 24 24" aria-hidden="true"><circle cx="12" cy="12" r="11" fill="#fff"/><rect x="6" y="8" width="12" height="8.5" fill="none" stroke="#062f66" stroke-width="1.6"/><path d="M6 8l6 5 6-5" fill="none" stroke="#062f66" stroke-width="1.6"/></svg>
          dylan@belvorahomes.com
        </li>
      </ul>
    </div>
  </section>
</body>
</html>
```